Design a WordPress layout for a home loans company

The home loans company in question is going through a rebrand and needs a new website layout.
Sites they like: http://www.brightkeylending.example.au/
Current logo: Attached.
Colours to be used: As per those used in logo.
Primary: #71aa3d
Secondary: #130e10
Pages to be designed:
- Homepage
- Internal services page
Menu items for display purposes:
- Home
- About Us
- Speak to a Broker
- Articles
- Contact Us
A modern design with simplicity is key.
For copy, dummy text such as Lorem ipsum will be fine.
If you would like anything elso, please ask.
Target Market(s)
25-40 year old
Mostly female
Buying their first home in most cases
Industry/Entity Type
Mortgage Brokerage
Number of Pages Required
2 page

```html
<!DOCTYPE html>
<html lang="en">
<head>
<meta charset="utf-8">
<title>Brightkey Lending — Home</title>
<link href="https://fonts.googleapis.com/css2?family=Oswald:wght@500;600&family=Open+Sans:wght@400;600;700;800&display=swap" rel="stylesheet">
<style>
:root{
  --green:#71aa3d;
  --green-dark:#5e9130;
  --ink:#130e10;
  --charcoal:#1e1b1c;
  --text:#555;
  --muted:#8a8a8a;
  --light:#f2f2f2;
  --white:#fff;
}
*{box-sizing:border-box;margin:0;padding:0}
html,body{width:1200px;height:2584px;overflow:hidden}
body{font-family:"Open Sans",Arial,sans-serif;color:var(--text);background:var(--white);position:relative}
.abs{position:absolute}
a{color:inherit;text-decoration:none}

/* header */
.site-header{left:0;top:0;width:1200px;height:128px;background:var(--white)}
.brand{left:64px;top:26px;display:flex;align-items:center;gap:14px}
.brand-mark{width:22px;height:22px;background:var(--green)}
.brand-name{font-family:"Open Sans",sans-serif;font-weight:800;font-size:34px;color:var(--ink);letter-spacing:-.5px}
.main-nav{right:60px;top:54px;display:flex;gap:46px;font-size:14px;font-weight:600;color:var(--ink);letter-spacing:.5px}
.main-nav .active{color:var(--green)}

/* hero */
.hero{left:0;top:128px;width:1200px;height:576px;background:linear-gradient(135deg,#8a8f93 0%,#6d6a66 40%,#4e4a46 70%,#7a6f68 100%)}
.hero-title{left:0;top:244px;width:1200px;text-align:center;font-family:Oswald,sans-serif;font-weight:600;font-size:58px;line-height:60px;color:var(--white);letter-spacing:1px;text-shadow:0 2px 6px rgba(0,0,0,.35)}
.btn{display:inline-block;background:var(--green);color:var(--white);font-weight:700;font-size:14px;letter-spacing:.5px;text-align:center}
.hero-btn{left:535px;top:456px;width:130px;height:42px;line-height:42px}
.hero-arrow{top:388px;width:20px;height:30px}
.finder{left:0;top:628px;width:1200px;height:76px;background:rgba(19,14,16,.85)}
.finder-label{left:0;top:628px;width:300px;height:76px;background:var(--green);color:var(--white);font-weight:800;font-size:20px;line-height:24px;padding:14px 0 0 26px;clip-path:polygon(0 0,100% 0,88% 100%,0 100%)}
.finder-input{top:646px;height:40px;background:var(--white);font-size:13px;color:var(--muted);padding:11px 12px}
.finder-btn{left:818px;top:646px;width:262px;height:40px;line-height:40px}

/* benefits */
.benefits-title{left:0;top:764px;width:1200px;text-align:center;font-weight:700;font-size:30px;color:var(--ink)}
.benefit{top:848px;width:300px;text-align:center}
.benefit svg{display:block;margin:0 auto 14px}
.benefit h3{font-size:20px;font-weight:700;color:var(--ink);margin-bottom:8px}
.benefit p{font-size:14px;line-height:20px;color:var(--muted)}

/* about / speak */
.about{left:0;top:1080px;width:1200px;height:340px;background:var(--light)}
.section-heading{font-size:24px;font-weight:800;color:var(--ink);letter-spacing:.5px}
.section-heading span{color:var(--green)}
.about-copy{left:72px;top:1120px;width:480px}
.about-copy p,.speak-copy p{font-size:14px;line-height:21px;color:var(--text);margin-top:16px}
.about-btn{left:72px;top:1320px;width:124px;height:40px;line-height:40px}
.about-photo{left:540px;top:1080px;width:660px;height:340px;background:linear-gradient(120deg,#c9c7c4 0%,#8d8781 45%,#5a6a73 100%);clip-path:polygon(18% 0,100% 0,100% 100%,0 100%)}
.speak-photo{left:0;top:1420px;width:760px;height:340px;background:linear-gradient(110deg,#7b5a47 0%,#b18b6e 40%,#6c7b8a 80%,#9aa3aa 100%)}
.speak-panel{left:560px;top:1420px;width:640px;height:340px;background:var(--white);clip-path:polygon(20% 0,100% 0,100% 100%,0 100%)}
.speak-copy{left:724px;top:1464px;width:420px}
.speak-btn{left:724px;top:1680px;width:124px;height:40px;line-height:40px}

/* articles */
.articles-title{left:0;top:1822px;width:1200px;text-align:center}
.article{top:1868px;width:340px}
.article-photo{width:340px;height:190px}
.article h4{font-size:16px;font-weight:800;color:var(--green);line-height:20px;margin-top:14px}
.article p{font-size:13px;line-height:19px;color:var(--muted);margin-top:10px}
.article .more{font-size:13px;font-weight:700;color:var(--ink);margin-top:12px;display:block}

/* footer */
.site-footer{left:0;top:2260px;width:1200px;height:324px;background:var(--charcoal)}
.footer-brand{left:64px;top:2290px;display:flex;align-items:center;gap:12px}
.footer-brand .brand-name{color:var(--white);font-size:30px}
.footer-about{left:64px;top:2360px;width:340px;font-size:12px;line-height:18px;color:#aaa}
.footer-copy{left:64px;top:2510px;font-size:11px;color:#888}
.subscribe{left:440px;top:2290px;width:760px;height:64px;background:var(--green);clip-path:polygon(5% 0,100% 0,100% 100%,0 100%)}
.subscribe-label{left:560px;top:2310px;font-size:20px;font-weight:800;color:var(--white);letter-spacing:.5px}
.subscribe-input{left:764px;top:2307px;width:250px;height:30px;background:var(--white);font-size:12px;color:var(--muted);padding:7px 10px}
.subscribe-btn{left:1024px;top:2307px;width:100px;height:30px;line-height:30px;background:var(--ink);color:var(--white);font-size:12px;font-weight:700;text-align:center}
.footer-col{top:2380px;width:200px}
.footer-col h5{font-size:13px;font-weight:700;color:var(--white);letter-spacing:.5px;margin-bottom:12px}
.footer-col li{list-style:none;font-size:12px;line-height:22px;color:#aaa}
</style>
</head>
<body>

<header class="site-header abs">
  <div class="brand abs"><span class="brand-mark"></span><span class="brand-name">Brightkey Lending</span></div>
  <nav class="main-nav abs">
    <a class="active">HOME</a><a>ABOUT US</a><a>SPEAK TO BROKER</a><a>ARTICLES</a><a>CONTACT US</a>
  </nav>
</header>

<section class="hero abs" role="img" aria-label="Photo of a smiling couple shaking hands with a broker outside a house with a sold sign"></section>
<svg class="hero-arrow abs" style="left:70px" viewBox="0 0 20 30"><path d="M16 3 4 15l12 12" fill="none" stroke="#fff" stroke-width="3"/></svg>
<svg class="hero-arrow abs" style="left:1110px" viewBox="0 0 20 30"><path d="M4 3l12 12L4 27" fill="none" stroke="#fff" stroke-width="3"/></svg>
<h1 class="hero-title abs">PELLENTESQUE EGET NISL NEC<br>IPSUM SCELERISQUE</h1>
<a class="btn hero-btn abs">READ MORE</a>

<div class="finder abs"></div>
<div class="finder-label abs">FIND A LOCAL<br>BROKER</div>
<div class="finder-input abs" style="left:316px;width:230px">Enter Location</div>
<div class="finder-input abs" style="left:586px;width:200px">Post Code</div>
<a class="btn finder-btn abs">FIND BROKER</a>

<h2 class="benefits-title abs">With a Brightkey Lending broker, you'll have</h2>
<div class="benefit abs" style="left:100px">
  <svg width="34" height="44" viewBox="0 0 34 44"><path d="M17 0C7.6 0 0 7.6 0 17c0 12 17 27 17 27s17-15 17-27C34 7.6 26.4 0 17 0z" fill="var(--green)"/><circle cx="17" cy="16" r="6.5" fill="#fff"/></svg>
  <h3>Local Experts</h3>
  <p>Lorem ipsum dolor sit amet, consectetur adipiscing elit. Nam et convallis ipsum.</p>
</div>
<div class="benefit abs" style="left:450px">
  <svg width="56" height="44" viewBox="0 0 56 44"><circle cx="28" cy="10" r="8" fill="var(--green)"/><circle cx="11" cy="16" r="6" fill="var(--green)"/><circle cx="45" cy="16" r="6" fill="var(--green)"/><path d="M14 44c0-12 6-18 14-18s14 6 14 18z" fill="var(--green)"/><path d="M0 44c0-10 5-15 11-15 3 0 5 1 6 2-3 3-5 8-5 13zM56 44c0-10-5-15-11-15-3 0-5 1-6 2 3 3 5 8 5 13z" fill="var(--green)"/></svg>
  <h3>Ongoing Trusted Advice</h3>
  <p>Lorem ipsum dolor sit amet, consectetur adipiscing elit. Nam et convallis ipsum.</p>
</div>
<div class="benefit abs" style="left:800px">
  <svg width="44" height="44" viewBox="0 0 44 44"><rect x="0" y="18" width="10" height="26" fill="var(--green)"/><path d="M14 20 24 2c4 0 6 3 5 7l-2 8h13c3 0 5 3 4 6l-4 17c-1 3-3 4-6 4H14z" fill="var(--green)"/></svg>
  <h3>Greater Choice</h3>
  <p>Lorem ipsum dolor sit amet, consectetur adipiscing elit. Nam et convallis ipsum.</p>
</div>

<section class="about abs"></section>
<div class="about-copy abs">
  <h2 class="section-heading">ABOUT <span>BRIGHTKEY LENDING</span></h2>
  <p>Lorem ipsum dolor sit amet, consectetur adipiscing elit. Nam et convallis ipsum. Phasellus sollicitudin tellus faucibus interdum tempor. Nulla at lacus vel libero tincidunt pharetra. Pellentesque nec mollis mi. Aliquam consectetur tellus tortor, in mollis nibh commodo quis. Aenean nec velit id mauris rhoncus dapibus in et erat. Phasellus sollicitudin tellus faucibus interdum tempor.</p>
</div>
<a class="btn about-btn abs">READ MORE</a>
<div class="about-photo abs" role="img" aria-label="Photo of a broker meeting a couple at a desk with a laptop"></div>

<div class="speak-photo abs" role="img" aria-label="Photo of a happy family standing in front of their new home"></div>
<div class="speak-panel abs"></div>
<div class="speak-copy abs">
  <h2 class="section-heading">SPEAK TO <span>BROKER</span></h2>
  <p>Lorem ipsum dolor sit amet, consectetur adipiscing elit. Nam et convallis ipsum. Phasellus sollicitudin tellus faucibus interdum tempor. Pellentesque nec mollis mi. Aliquam consectetur tellus tortor, in mollis nibh commodo quis. Aenean nec velit id mauris rhoncus dapibus in et erat. Phasellus sollicitudin tellus faucibus interdum tempor.</p>
</div>
<a class="btn speak-btn abs">READ MORE</a>

<h2 class="section-heading articles-title abs">RECENT <span>ARTICLES</span></h2>
<article class="article abs" style="left:72px">
  <div class="article-photo" role="img" aria-label="Photo of a model house with keys on a desk" style="background:linear-gradient(135deg,#d8c8a8,#9b8a6e)"></div>
  <h4>SED MAXIMUS FEUGIAT MAURIS AT BIBENDUM VEHICULA</h4>
  <p>Nunc sollicitudin tempor ante. Mauris faucibus tincidunt massa, et hendrerit ligula dapibus sit amet vulputate.</p>
  <span class="more">Read More &gt;&gt;</span>
</article>
<article class="article abs" style="left:430px">
  <div class="article-photo" role="img" aria-label="Photo of a couple reviewing loan papers at home" style="background:linear-gradient(135deg,#c3b8ab,#6f6a66)"></div>
  <h4>SED MAXIMUS FEUGIAT MAURIS AT BIBENDUM VEHICULA</h4>
  <p>Nunc sollicitudin tempor ante. Mauris faucibus tincidunt massa, et hendrerit ligula dapibus sit amet vulputate.</p>
  <span class="more">Read More &gt;&gt;</span>
</article>
<article class="article abs" style="left:788px">
  <div class="article-photo" role="img" aria-label="Photo of a handshake with a small house model" style="background:linear-gradient(135deg,#b9c2c8,#5c5550)"></div>
  <h4>SED MAXIMUS FEUGIAT MAURIS AT BIBENDUM VEHICULA</h4>
  <p>Nunc sollicitudin tempor ante. Mauris faucibus tincidunt massa, et hendrerit ligula dapibus sit amet vulputate.</p>
  <span class="more">Read More &gt;&gt;</span>
</article>

<footer class="site-footer abs"></footer>
<div class="footer-brand abs"><span class="brand-mark"></span><span class="brand-name">Brightkey Lending</span></div>
<p class="footer-about abs">Lorem ipsum dolor sit amet, consectetur adipiscing elit. Nam et convallis ipsum. Phasellus sollicitudin tellus faucibus interdum tempor nulla.</p>
<p class="footer-copy abs">Copyright © 2016, Company Name</p>
<div class="subscribe abs"></div>
<div class="subscribe-label abs">EMAIL SUBSCRIBE</div>
<div class="subscribe-input abs">Enter Email Address</div>
<div class="subscribe-btn abs">SIGN UP</div>
<div class="footer-col abs" style="left:560px">
  <h5>SITE MAP</h5>
  <ul><li>Home</li><li>About Us</li><li>Speak to Broker</li><li>Articles</li><li>Contact Us</li></ul>
</div>
<div class="footer-col abs" style="left:760px">
  <h5>RESOURCES</h5>
  <ul><li>Sub-item one</li><li>Sub-item two</li><li>Sub-item three</li><li>Sub-item four</li></ul>
</div>
<div class="footer-col abs" style="left:960px;width:220px">
  <h5>CONTACT INFO</h5>
  <ul><li style="color:#fff;font-weight:700">BRIGHTKEY LENDING</li><li>Aenean nec velit 12</li><li>Mauris VIC 3000</li><li>1 300 555 018</li><li>info@brightkeylending.example.au</li></ul>
</div>

</body>
</html>
```